Business Card Design Project

Business Card
We are rebranding with a new logo
Industry/Entity Type
Business
Contact Information for Business Card
Dennis Marlow +61 427581962 dennis@qovo.com.au P.O. Box 872 Kelvindale QLD 4309
Requirements
Must have
- Logo

```html
<!DOCTYPE html>
<html lang="en">
<head>
<meta charset="utf-8">
<title>Qovo International – Business Card</title>
<link rel="stylesheet" href="https://fonts.googleapis.com/css2?family=Dancing+Script:wght@600&family=Roboto:wght@400;500;700&display=swap">
<style>
  :root {
    --page-bg: #e2e2e2;
    --card-bg: #f8f8f8;
    --card-edge: #d6d6d6;
    --brand-navy: #14547a;
    --text-dark: #222222;
    --accent-orange: #e0661f;
    --brand-blue: #1f8fcf;
  }
  * { margin: 0; padding: 0; box-sizing: border-box; }
  html, body {
    width: 1200px;
    height: 576px;
    overflow: hidden;
    background: var(--page-bg);
    font-family: "Roboto", Arial, sans-serif;
  }
  .stage {
    position: relative;
    width: 1200px;
    height: 576px;
  }
  .card {
    position: absolute;
    top: 140px;
    width: 482px;
    height: 292px;
    background: var(--card-bg);
    border: 1px solid var(--card-edge);
    border-radius: 12px;
  }
  .card--front { left: 82px; }
  .card--back { left: 602px; }

  .brand {
    display: flex;
    align-items: center;
    gap: 10px;
    color: var(--brand-navy);
    font-weight: 700;
    letter-spacing: 0.04em;
    white-space: nowrap;
  }
  .brand-dot {
    flex: none;
    border-radius: 50%;
    background: var(--brand-blue);
  }
  .card--front .brand {
    position: absolute;
    left: 0;
    right: 0;
    top: 128px;
    justify-content: center;
    font-size: 28px;
  }
  .card--front .brand-dot { width: 22px; height: 22px; }

  .card--back .brand {
    position: absolute;
    right: 30px;
    top: 74px;
    font-size: 17px;
    gap: 7px;
  }
  .card--back .brand-dot { width: 14px; height: 14px; }

  .holder-name {
    position: absolute;
    left: 24px;
    top: 32px;
    font-family: "Dancing Script", cursive;
    font-weight: 600;
    font-size: 26px;
    color: var(--brand-navy);
  }
  .holder-role {
    position: absolute;
    left: 25px;
    top: 70px;
    font-size: 11.5px;
    color: var(--text-dark);
  }
  .contact-list {
    position: absolute;
    left: 28px;
    top: 213px;
    list-style: none;
  }
  .contact-item {
    display: flex;
    align-items: center;
    height: 17px;
    font-size: 12.5px;
    color: var(--text-dark);
  }
  .contact-icon {
    width: 11px;
    height: 11px;
    margin-right: 11px;
    fill: var(--accent-orange);
  }
</style>
</head>
<body>
<main class="stage">
  <section class="card card--front" aria-label="Card front">
    <div class="brand"><span class="brand-dot"></span>Qovo International</div>
  </section>

  <section class="card card--back" aria-label="Card back">
    <h1 class="holder-name">Dennis Marlow</h1>
    <p class="holder-role">Managing Director</p>
    <div class="brand"><span class="brand-dot"></span>Qovo International</div>
    <ul class="contact-list">
      <li class="contact-item">
        <svg class="contact-icon" viewBox="0 0 12 12" aria-hidden="true">
          <path d="M1 4.5c0-2 2-3 5-3s5 1 5 3v1H8.5V4.3c-.8-.4-4.2-.4-5 0V5.5H1z"/>
          <path d="M3 6h6l1.5 4.5h-9z"/>
        </svg>+61 427581962
      </li>
      <li class="contact-item">
        <svg class="contact-icon" viewBox="0 0 12 12" aria-hidden="true">
          <path d="M0.5 2.5h11v7h-11z"/>
          <path d="M1 3l5 3.8L11 3" fill="none" stroke="#f8f8f8" stroke-width="1"/>
        </svg>dennis@qovo.com.au
      </li>
      <li class="contact-item">
        <svg class="contact-icon" viewBox="0 0 12 12" aria-hidden="true">
          <path d="M6 0.5a4 4 0 0 0-4 4c0 3 4 7 4 7s4-4 4-7a4 4 0 0 0-4-4zm0 2.3a1.7 1.7 0 1 1 0 3.4 1.7 1.7 0 0 1 0-3.4z" fill-rule="evenodd"/>
        </svg>P.O. Box 872 Kelvindale QLD 4309
      </li>
    </ul>
  </section>
</main>
</body>
</html>
```